Marn-ridge Tide Harbor Custom Brokers Limited

Name: Dorvella Hastings
Title: Customs Broker
Address: Shop 9 Birchfield Commercial Complex
207-209 Harlow Road
Kingston 8
Telephone: (876)
Email: tideharborport@quillmail.example

```html
<!DOCTYPE html>
<html lang="en">
<head>
<meta charset="utf-8">
<title>Marn-ridge Tide Harbor Custom Brokers Limited – Business Card</title>
<link rel="stylesheet" href="https://fonts.googleapis.com/css2?family=Montserrat:wght@700;800&family=Lato:wght@400;700&display=swap">
<style>
  :root {
    --navy: #142e54;
    --gold: #eba91e;
    --white: #ffffff;
    --grey-text: #6d6e71;
    --stage: #3b3c3f;
  }
  * { box-sizing: border-box; margin: 0; padding: 0; }
  html, body { width: 1200px; height: 900px; overflow: hidden; }
  body {
    background: var(--stage);
    font-family: "Lato", sans-serif;
    display: flex;
    flex-direction: column;
    align-items: center;
    justify-content: center;
    gap: 60px;
  }
  .card {
    position: relative;
    width: 640px;
    height: 366px;
    border-radius: 28px;
    overflow: hidden;
  }

  /* Back side */
  .card-back {
    background: var(--navy);
    display: flex;
    align-items: center;
    justify-content: center;
  }
  .brand {
    display: flex;
    align-items: center;
    gap: 16px;
  }
  .brand-dot {
    flex: none;
    width: 22px;
    height: 22px;
    border-radius: 50%;
    background: var(--gold);
  }
  .brand-name {
    font-family: "Montserrat", sans-serif;
    font-weight: 700;
    line-height: 1.2;
  }
  .card-back .brand-name {
    color: var(--white);
    font-size: 26px;
    max-width: 380px;
  }

  /* Front side */
  .card-front { background: var(--white); }
  .card-front .wave {
    position: absolute;
    inset: 0;
    width: 100%;
    height: 100%;
  }
  .card-front .brand {
    position: absolute;
    top: 66px;
    right: 40px;
    gap: 10px;
  }
  .card-front .brand-dot { width: 14px; height: 14px; }
  .card-front .brand-name {
    color: var(--navy);
    font-size: 16px;
    max-width: 210px;
  }
  .person {
    position: absolute;
    left: 40px;
    top: 150px;
  }
  .person-name {
    font-family: "Montserrat", sans-serif;
    font-weight: 800;
    font-size: 30px;
    color: var(--navy);
    letter-spacing: -0.3px;
  }
  .person-name .surname { color: var(--gold); }
  .person-title {
    margin-top: 4px;
    font-size: 19px;
    color: var(--grey-text);
  }
  .contact {
    position: absolute;
    left: 310px;
    top: 252px;
    color: var(--white);
    font-size: 14.5px;
    line-height: 20px;
    font-style: normal;
  }
  .contact-line {
    display: flex;
    align-items: center;
    gap: 8px;
    white-space: nowrap;
  }
  .contact-line.has-icon { margin-left: -26px; }
  .contact-icon { width: 18px; height: 18px; flex: none; }
</style>
</head>
<body>

  <section class="card card-back" aria-label="Business card, back">
    <div class="brand">
      <span class="brand-dot"></span>
      <span class="brand-name">Marn-ridge Tide Harbor Custom Brokers Limited</span>
    </div>
  </section>

  <section class="card card-front" aria-label="Business card, front">
    <svg class="wave" viewBox="0 0 640 366" preserveAspectRatio="none" aria-hidden="true">
      <path d="M170 366 C210 280 300 232 470 226 C590 222 630 140 640 40 L640 366 Z" fill="var(--navy)"/>
      <path d="M146 366 C190 266 300 212 455 212" fill="none" stroke="var(--gold)" stroke-width="7" stroke-linecap="round"/>
    </svg>

    <div class="brand">
      <span class="brand-dot"></span>
      <span class="brand-name">Marn-ridge Tide Harbor Custom Brokers Limited</span>
    </div>

    <div class="person">
      <p class="person-name">Dorvella <span class="surname">Hastings</span></p>
      <p class="person-title">Customs Broker</p>
    </div>

    <address class="contact">
      <p class="contact-line">Shop 9 Birchfield Commercial Complex</p>
      <p class="contact-line">207-209 Harlow Road</p>
      <p class="contact-line">Kingston 8</p>
      <p class="contact-line has-icon">
        <svg class="contact-icon" viewBox="0 0 24 24" aria-hidden="true">
          <path d="M6.6 10.8a15 15 0 0 0 6.6 6.6l2.2-2.2a1 1 0 0 1 1-.25 11.4 11.4 0 0 0 3.6.57 1 1 0 0 1 1 1V20a1 1 0 0 1-1 1A17 17 0 0 1 3 4a1 1 0 0 1 1-1h3.5a1 1 0 0 1 1 1c0 1.25.2 2.45.57 3.6a1 1 0 0 1-.25 1z" fill="var(--gold)"/>
        </svg>
        (876) 555 0142
      </p>
      <p class="contact-line has-icon">
        <svg class="contact-icon" viewBox="0 0 24 24" aria-hidden="true">
          <rect x="2" y="5" width="20" height="14" rx="1.5" fill="var(--gold)"/>
          <path d="M3 6l9 7 9-7" fill="none" stroke="var(--navy)" stroke-width="1.6"/>
        </svg>
        tideharborport@quillmail.example
      </p>
    </address>
  </section>

</body>
</html>
```